Website Re-Design

We would like to explore the possibility of a re-design of our website. We want all the content that it currently has to remain on the pages, and we don't want our logo/corporate identity or colours changed, so it is literally just a website re-design.

Our website is www.drelvix.co.uk

Websites that we like are

http://www.tarnwillow.co.uk/
http://quomplet.com/

```html
<!DOCTYPE html>
<html lang="en">
<head>
<meta charset="utf-8">
<title>Drelvix – Inbound Marketing &amp; SEO Performance Agency</title>
<link rel="stylesheet" href="https://fonts.googleapis.com/css2?family=Ubuntu:wght@300;400;500;700&family=Open+Sans:ital,wght@0,400;0,600;1,400&display=swap">
<style>
:root{
  --pink:#d6127f;
  --green:#8cc63f;
  --teal:#13a89e;
  --teal-dark:#0e8f86;
  --ink:#333;
  --muted:#555;
  --light:#ececec;
  --rule:#d6d6d6;
  --grey:#7a7a7a;
  --footer:#5a5a5a;
  --bar:#4a4a4a;
  --white:#fff;
}
*{margin:0;padding:0;box-sizing:border-box}
html,body{width:1200px;height:2525px;overflow:hidden;background:var(--white)}
body{position:relative;font-family:"Open Sans",Arial,sans-serif;color:var(--ink)}
.abs{position:absolute}
.head{font-family:"Ubuntu",Arial,sans-serif;font-weight:400}
.center{left:0;width:1200px;text-align:center}

/* header */
.site-header{top:0;left:0;width:1200px;height:76px;background:var(--white);box-shadow:0 2px 4px rgba(0,0,0,.12);z-index:2}
.brand{font-family:"Ubuntu",sans-serif;font-weight:700;color:var(--pink);letter-spacing:1px}
.site-header .brand{left:173px;top:22px;font-size:31px}
.nav a{position:absolute;top:29px;height:27px;line-height:27px;font-size:11.5px;color:#666;text-decoration:none;font-family:"Open Sans",sans-serif}
.nav .active{background:var(--green);color:var(--white);padding:0 18px;border-radius:2px}

/* hero */
.hero{top:76px;left:0;width:1200px;height:399px;background:radial-gradient(ellipse at 45% 45%,#ffffff 0%,#f1f1f1 60%,#e4e4e4 100%)}
.hero-art{left:80px;top:112px;width:580px;height:385px;border-radius:8px;background:linear-gradient(135deg,#d7f0ee 0%,#e9e9ec 50%,#f7dcea 100%)}
.hero-title{left:671px;top:214px;font-family:"Ubuntu",sans-serif;font-weight:500;font-size:22px;line-height:31px;text-transform:uppercase}
.btn{display:block;text-align:center;text-decoration:none;border-radius:2px}
.btn-teal{background:var(--teal);color:var(--white);box-shadow:0 2px 0 var(--teal-dark)}
.dots{left:962px;top:441px;display:flex;gap:3px}
.dots span{width:10px;height:10px;border-radius:50%;background:var(--teal)}
.dots span:first-child{background:var(--pink)}

/* intro */
.intro .brand{font-size:32px;top:556px}
.tagline{top:607px;font-size:15px;color:var(--ink);letter-spacing:.3px}
.lead{top:640px;font-size:12px;line-height:20px;color:var(--muted)}

/* services */
.services{top:715px;left:0;width:1200px;height:387px;background:var(--light)}
.section-title{font-family:"Ubuntu",sans-serif;color:var(--pink);font-size:25px}
.laptop{left:173px;top:826px;width:394px;height:229px;border-radius:10px 10px 4px 4px;background:linear-gradient(180deg,#7fa7d4 0%,#b9cde0 55%,#8c8f93 100%)}
.services-copy{left:613px;top:826px;width:405px;font-size:11px;line-height:17px;color:var(--muted)}
.services-copy p+p{margin-top:17px}

/* works */
.works-lead{top:1168px;font-size:12px;line-height:21px;color:var(--muted)}
.rule{left:173px;top:1230px;width:857px;height:1px;background:var(--rule)}
.card{top:1266px;width:256px}
.card .thumb{height:178px}
.card h3{margin-top:24px;font-family:"Ubuntu",sans-serif;font-weight:400;font-size:12.5px;line-height:21px;color:var(--pink);text-transform:uppercase}
.card .tags{margin-top:8px;font-size:10px;font-style:italic;color:#666}
.arrow{color:#c4c4c4;font-size:22px;font-family:"Ubuntu",sans-serif}

/* cta */
.cta{top:1573px;left:0;width:1200px;height:196px;background:var(--teal);color:var(--white)}
.cta-sub{left:173px;top:1657px;font-family:"Ubuntu",sans-serif;font-size:21px}
.cta-copy{left:173px;top:1697px;width:620px;font-size:12px;line-height:21px}
.btn-white{left:823px;top:1687px;width:204px;height:43px;line-height:43px;background:var(--white);color:#666;font-family:"Ubuntu",sans-serif;font-size:16px}

/* clients */
.client{top:1924px;width:185px;height:113px;border:2px solid #e1e1e1;display:flex;align-items:center;justify-content:center;gap:8px;font-family:"Ubuntu",sans-serif;font-size:17px;color:#555}
.client i{width:14px;height:14px;background:var(--teal);display:block}

/* about */
.about{top:2080px;left:0;width:1200px;height:219px;background:var(--grey);color:var(--white)}
.about h2{font-family:"Ubuntu",sans-serif;font-weight:300;font-size:27px}
.about p{font-size:10px;line-height:20px}
.divider{left:599px;top:2118px;width:1px;height:140px;background:#929292}

/* footer */
.footer{top:2299px;left:0;width:1200px;height:178px;background:var(--footer);color:var(--white)}
.footer h4{font-family:"Ubuntu",sans-serif;font-weight:400;font-size:13px}
.footer ul{list-style:none;font-size:10px;line-height:20px}
.contact-line{font-size:10px;line-height:18px;display:flex;gap:10px;align-items:flex-start}
.social{display:flex;align-items:center;gap:8px;font-size:10px}
.social i{width:26px;height:26px;border-radius:50%;border:1px solid #888;background:#666;display:block}
.bottom-bar{top:2477px;left:0;width:1200px;height:48px;background:var(--bar);color:#ddd;font-size:10px;line-height:48px}
</style>
</head>
<body>

<header class="abs site-header">
  <div class="abs brand">DRELVIX</div>
  <nav class="nav">
    <a class="active" style="left:518px">HOME</a>
    <a style="left:628px">ABOUT</a>
    <a style="left:719px">PORTFOLIO</a>
    <a style="left:834px">WHAT WE DO</a>
    <a style="left:958px">CONTACT US</a>
  </nav>
</header>

<section class="abs hero">
</section>
<div class="abs hero-art" role="img" aria-label="Illustration of a leafy tree beside a desktop monitor, tablet and phone showing the agency name"></div>
<h1 class="abs hero-title head" style="font-weight:500">
  <span style="color:var(--pink)">Drelvix takes a holistic view </span><span style="color:var(--green)">of earning</span><br>
  <span style="color:var(--green)">your </span><span style="color:var(--teal)">customers attention</span>
</h1>
<a class="abs btn btn-teal" style="left:682px;top:288px;width:141px;height:40px;line-height:40px;font-size:13px">TALK TO US</a>
<div class="abs dots"><span></span><span></span><span></span><span></span></div>

<section class="intro">
  <div class="abs center brand">DRELVIX</div>
  <div class="abs center tagline">YOUR&nbsp; INBOUND MARKETING &amp; SEO PERFORMANCE AGENCY</div>
  <p class="abs center lead">Do you want to earn your customers attention? Gain more visibility in the SERPs and build &amp; engage with your audience?<br>Drelvix specialises in SEO, Social media, CRO and Design &amp; Creative services. Offering a bespoke and personal service from a team of digital natives.</p>
</section>

<section class="abs services"></section>
<h2 class="abs center section-title" style="top:750px">What can we do for you?</h2>
<div class="abs laptop" role="img" aria-label="Laptop showing a businessman with binoculars looking over a city skyline"></div>
<div class="abs services-copy">
  <p>It's all about people. You need to consider Search and Social as an unmissable opportunity to engage with existing and future customers.Your audience is online, socialising, working and buying. Having a digital strategy to be found, to actively engage and retain customers is essential.</p>
  <p>Here at Drelvix, we take a 360 degree approach to inbound marketing. We ensure that you are found in an ever increasingly personalised and curated version of the internet.</p>
</div>
<a class="abs btn btn-teal" style="left:616px;top:995px;width:207px;height:43px;line-height:43px;font-size:14px">Click here for more Info</a>

<h2 class="abs center section-title" style="top:1127px">Recent Works</h2>
<p class="abs center works-lead">Check out our recent works and case-studies. These are a few examples to show the diversity of work that we can do to earn real attention, generate inbound links,<br>mentions, citations and be used across many of our marketing channels. See more on our portfolio page and learn about what we could do for you.</p>
<div class="abs rule"></div>
<div class="abs arrow" style="left:124px;top:1339px">&#8249;</div>
<div class="abs arrow" style="left:1066px;top:1339px">&#8250;</div>
<article class="abs card" style="left:173px">
  <div class="thumb" role="img" aria-label="Campaign screens on a monitor over a blue backdrop" style="background:linear-gradient(135deg,#4fb8e6,#e8ecef 60%,#f3c9b8)"></div>
  <h3>Biggest baddest bucklet list<br>– Wayfarer Trails</h3><div class="tags">Branding &amp; PR, SEO, Social</div>
</article>
<article class="abs card" style="left:473px">
  <div class="thumb" role="img" aria-label="Campaign pages on a tablet over a pink backdrop" style="background:linear-gradient(135deg,#ea4fa1,#3a4658 50%,#e8e0d0)"></div>
  <h3>Biggest baddest bucklet list<br>– Wayfarer Trails</h3><div class="tags">Branding &amp; PR, SEO, Social</div>
</article>
<article class="abs card" style="left:773px">
  <div class="thumb" role="img" aria-label="Campaign video page on a monitor over a green backdrop" style="background:linear-gradient(135deg,#7dbd4b,#e9ece6 55%,#b5432f)"></div>
  <h3>Biggest baddest bucklet list<br>– Wayfarer Trails</h3><div class="tags">Branding &amp; PR, SEO, Social</div>
</article>

<section class="abs cta"></section>
<h2 class="abs center head" style="top:1598px;font-size:27px;color:var(--white)">Sound interesting?</h2>
<div class="abs cta-sub" style="color:var(--white)">Interested in what you have seen so far?</div>
<p class="abs cta-copy" style="color:var(--white)">Are you looking for a progressive and innovative inbound marketing agency who can work alongside your existing teams. If Yes, then let's have a chat.</p>
<a class="abs btn btn-white">Connect with us</a>

<h2 class="abs center section-title" style="top:1805px">Our Clients</h2>
<p class="abs center works-lead" style="top:1853px">We work with and represent a number of progressive companies in their SEO, social, inbound marketing, content and strategy needs. Check<br>out our case-studies for examples.</p>
<div class="abs arrow" style="left:152px;top:1967px">&#8249;</div>
<div class="abs arrow" style="left:1036px;top:1967px">&#8250;</div>
<div class="abs client" style="left:195px"><i></i>Fernhollow</div>
<div class="abs client" style="left:405px"><i></i>CoachPortal</div>
<div class="abs client" style="left:614px"><i></i>Wayfarer Trails</div>
<div class="abs client" style="left:821px"><i></i>Staynest</div>

<section class="abs about">
  <h2 class="abs" style="left:207px;top:32px">About Us</h2>
  <p class="abs" style="left:207px;top:80px;width:340px">Drelvix is an inbound marketing agency offering a raft of services from digital strategy and planning through to SEO, Social media, SMM, CRO, Design &amp; Creative, through to paid for performance campaigns.</p>
  <h2 class="abs" style="left:207px;top:150px">Talk to us <span style="font-size:14px">to discuss your needs.</span></h2>
  <h2 class="abs" style="left:653px;top:32px">Where are we?</h2>
  <p class="abs" style="left:653px;top:80px;width:330px">We are in London, UK, based down the best mews in Canal Row, so come check it out and walk the canals with us or we're happy to venture to you!We are in London, UK, based down the best mews in Canal Row, so come check it out and walk the canals with us or we're happy to venture to you!</p>
</section>
<div class="abs divider"></div>

<footer class="abs footer">
  <div class="abs brand" style="left:180px;top:76px;font-size:28px;color:#8d8d8d">DRELVIX</div>
  <h4 class="abs" style="left:372px;top:30px">Useful Links</h4>
  <ul class="abs" style="left:373px;top:55px"><li>Home</li><li>About</li><li>Portfolio</li><li>What We Do</li><li>Contact Us</li></ul>
  <h4 class="abs" style="left:544px;top:30px">Uk Office</h4>
  <div class="abs" style="left:522px;top:60px;width:200px">
    <div class="contact-line"><svg width="10" height="12" viewBox="0 0 10 12"><path d="M5 0a4 4 0 0 1 4 4c0 3-4 8-4 8S1 7 1 4a4 4 0 0 1 4-4z" fill="#ccc"/><circle cx="5" cy="4" r="1.5" fill="#5a5a5a"/></svg><span>7 Marlow Yard, Canal Row,<br>London, UK, W2 9QX</span></div>
    <div class="contact-line" style="margin-top:8px"><svg width="11" height="11" viewBox="0 0 11 11"><path d="M2 0l2 2.5-1 1.5c.7 1.5 2 2.8 3.5 3.5l1.5-1L10.5 9 9 11C4 10.5.5 7 0 2z" fill="#ccc"/></svg><span>Phone: +44 (0) 207 946 0321</span></div>
    <div class="contact-line" style="margin-top:8px"><svg width="12" height="9" viewBox="0 0 12 9"><rect x=".5" y=".5" width="11" height="8" fill="none" stroke="#ccc"/><path d="M.5.5L6 5 11.5.5" fill="none" stroke="#ccc"/></svg><span>Email: hello@drelvix.co.uk</span></div>
  </div>
  <h4 class="abs" style="left:783px;top:30px">Connect With Us</h4>
  <div class="abs social" style="left:783px;top:68px"><i></i>: Chirpline</div>
  <div class="abs social" style="left:911px;top:68px"><i></i>: Linkfold</div>
  <div class="abs social" style="left:783px;top:112px"><i></i>: Plusring</div>
  <div class="abs social" style="left:911px;top:112px"><i></i>: Viewcast</div>
</footer>
<div class="abs bottom-bar center">Copyrights © 2013, Drelvix. All Rights Reserved.</div>

</body>
</html>
```